Company Website for an IT business called "BRIGHT HARBOR"

Complete website creation with text and graphics.
We need :
- modern and creative design for our IT company
- Content management system to edit text later on
- Integrate third party content from partner company
- Contact form (transfer by email)
Updates

Target Market(s)

Small and medium business
private customers

Industry/Entity Type

Information Technology

Coding

Coded - Design and coding required

Number of Pages Required

1 page

Font styles to use
Sans Serif

Requirements
Must have
• Contact form
Link to legal information
Link to data protection (GDPR)
Link to website owner declaration
Nice to have
• Fresh and creative graphics for IT business

```html
<!DOCTYPE html>
<html lang="en">
<head>
<meta charset="utf-8">
<title>Bright Harbor – IT Services</title>
<link rel="stylesheet" href="https://fonts.googleapis.com/css2?family=Poppins:ital,wght@0,400;0,500;0,600;1,400&display=swap">
<style>
:root{
  --black:#000;
  --blue:#1598e3;
  --blue-deep:#1183cf;
  --navy:#0a2a5c;
  --ink:#0a1423;
  --footer:#0b2346;
  --text:#3a3a3a;
  --muted:#6d6d6d;
  --white:#fff;
}
*{margin:0;padding:0;box-sizing:border-box}
html,body{width:1200px;height:3082px;overflow:hidden}
body{font-family:"Poppins",sans-serif;color:var(--text);background:var(--white);position:relative}
h1,h2,h3{font-weight:400}
.btn{position:absolute;display:flex;align-items:center;justify-content:center;background:var(--blue-deep);color:var(--white);border-radius:20px;font-size:13px;font-weight:500;text-transform:uppercase}

/* header */
.site-header{position:absolute;left:0;top:0;width:1200px;height:100px;background:var(--black)}
.brand{position:absolute;left:143px;top:34px;display:flex;align-items:center;gap:10px;color:var(--white);font-size:20px;font-weight:500;letter-spacing:2px}
.brand-mark{width:14px;height:14px;background:var(--white)}
.main-nav{position:absolute;top:40px;left:0;width:1200px;font-size:13px;color:var(--white)}
.main-nav span{position:absolute}
.quote-btn{left:921px;top:32px;width:133px;height:36px;background:var(--blue);font-size:15px;text-transform:none}

/* hero */
.hero{position:absolute;left:0;top:100px;width:1200px;height:526px;background:linear-gradient(120deg,#0d1a33 0%,#22406b 35%,#37506e 60%,#142640 100%)}
.hero-curve{position:absolute;left:0;top:100px}
.hero-kicker{position:absolute;top:212px;width:1200px;text-align:center;color:var(--white);font-size:22px;letter-spacing:3px}
.hero-title{position:absolute;top:232px;width:1200px;text-align:center;color:var(--blue);font-size:84px;font-weight:600;line-height:1}
.hero-sub{position:absolute;top:336px;width:1200px;text-align:center;color:var(--white);font-size:25px}
.hero-btn{left:535px;top:384px;width:130px;height:37px}

/* about */
.about-kicker{position:absolute;top:662px;width:1200px;text-align:center;font-size:20px;letter-spacing:3px;color:#222}
.about-title{position:absolute;top:692px;width:1200px;text-align:center;font-size:62px;font-weight:600;color:var(--blue-deep);line-height:1.1}
.about-sub{position:absolute;top:762px;width:1200px;text-align:center;font-size:26px;font-style:italic;color:var(--muted)}
.about-copy{position:absolute;left:180px;top:812px;width:840px;text-align:center;font-size:15px;line-height:28.8px;color:#444}
.about-btn{left:535px;top:1042px;width:130px;height:38px}

/* feature grid */
.tile{position:absolute;height:287px}
.panel{position:absolute;height:287px;color:var(--white)}
.panel h3{position:absolute;top:40px;font-size:24px;font-weight:400}
.panel p{position:absolute;top:90px;width:400px;font-size:14.5px;line-height:24px}
.panel .btn{top:188px;width:131px;height:37px;background:var(--blue-deep)}
.panel-blue{background:var(--blue)}
.panel-blue .btn{background:#1076c0}
.panel-ink{background:var(--ink)}
.panel-navy{background:var(--navy)}

/* testimonials */
.t-title{position:absolute;top:2036px;width:1184px;text-align:center;font-size:37px;font-weight:400;color:#111}
.t-sub{position:absolute;top:2088px;width:1200px;text-align:center;font-size:17px;font-style:italic;color:var(--muted)}
.t-card{position:absolute;left:145px;top:2145px;width:911px;height:332px;background:#f7f7f7;box-shadow:0 4px 14px rgba(0,0,0,.15)}
.t-photo{position:absolute;left:806px;top:2145px;width:250px;height:332px;background:linear-gradient(180deg,#9fb4c8,#5d7690 70%,#a9bccc)}
.t-quote{position:absolute;left:192px;top:2180px}
.t-text{position:absolute;left:192px;top:2244px;width:570px;font-size:19px;font-style:italic;line-height:29px;color:#8a8a8a}
.t-name{position:absolute;left:198px;top:2380px;font-size:22px;color:#555}
.t-city{position:absolute;left:198px;top:2419px;font-size:16px;color:#666}
.t-arrow{position:absolute;top:2294px;width:34px;height:34px;border-radius:50%}

/* footer */
.site-footer{position:absolute;left:0;top:2536px;width:1200px;height:546px;background:radial-gradient(ellipse at 50% 60%,#12386b 0%,var(--footer) 60%,#081a36 100%);clip-path:polygon(0 0,50% 64px,100% 0,100% 100%,0 100%)}
.footer-brand{position:absolute;top:2646px;width:1200px;display:flex;justify-content:center;align-items:center;gap:10px;color:var(--white);font-size:22px;font-weight:500;letter-spacing:2px}
.news-label{position:absolute;top:2702px;width:1200px;text-align:center;color:var(--white);font-size:16px}
.field{border:0;outline:0;background:var(--white);font-family:"Poppins",sans-serif;font-size:12px;color:#333;padding:0 12px;height:31px}
.field::placeholder{color:#888}
.send{border:0;background:var(--blue);color:var(--white);font-family:"Poppins",sans-serif;font-size:15px;font-weight:500;height:31px;cursor:pointer}
.newsletter-form{position:absolute;left:419px;top:2736px;display:flex;gap:8px}
.newsletter-form .field{width:240px}
.newsletter-form .send{width:114px;font-size:16px}
.contact-form{position:absolute;left:207px;top:2779px;width:786px;display:flex;gap:8px}
.contact-form .name{width:160px}
.contact-form .email{width:190px}
.contact-form .message{width:298px}
.contact-form .send{width:114px}
.contact-pill{position:absolute;left:207px;top:2824px;width:786px;height:48px;border:1px solid var(--blue);border-radius:24px;display:flex;align-items:center;justify-content:center;gap:18px;color:var(--white);font-size:17px}
.contact-pill svg{vertical-align:middle;margin-right:8px}
.footer-links{position:absolute;width:1200px;text-align:center;color:var(--white);font-size:13.5px}
.footer-links i{font-style:normal;margin:0 14px}
.social{position:absolute;top:2996px;left:536px;display:flex;gap:4px}
.social span{width:29px;height:29px;border:1.5px solid var(--white);border-radius:50%}
</style>
</head>
<body>

<header class="site-header">
  <div class="brand"><span class="brand-mark"></span>BRIGHT HARBOR</div>
  <nav class="main-nav">
    <span style="left:441px">Home</span>
    <span style="left:507px">About US</span>
    <span style="left:593px">Services</span>
    <span style="left:673px">Clients</span>
    <span style="left:745px">Projects</span>
    <span style="left:823px">Contact Us</span>
  </nav>
  <div class="btn quote-btn">Get A Quote</div>
</header>

<section>
  <div class="hero" role="img" aria-label="Team of IT professionals working at computers with glowing data overlay"></div>
  <svg class="hero-curve" width="1200" height="526" viewBox="0 0 1200 526">
    <path d="M0 526 L0 522 Q600 440 1200 522 L1200 526 Z" fill="#fff"/>
    <path d="M524 480 Q530 440 565 440 L635 440 Q670 440 676 480 Z" fill="#fff"/>
    <g fill="#7dbff0">
      <circle cx="563" cy="461" r="4"/><circle cx="580" cy="461" r="4"/>
      <circle cx="620" cy="461" r="4"/><circle cx="636" cy="461" r="4"/>
    </g>
    <circle cx="600" cy="461" r="7" fill="#1183cf"/>
  </svg>
  <div class="hero-kicker">Welcome to</div>
  <h1 class="hero-title">Bright Harbor</h1>
  <div class="hero-sub">Neque porro quisquam est qui dolorem</div>
  <div class="btn hero-btn">Learn More</div>
</section>

<section>
  <div class="about-kicker">About Us</div>
  <h2 class="about-title">Bright Harbor</h2>
  <div class="about-sub">Neque porro quisquam est qui dolorem</div>
  <p class="about-copy">Lorem Ipsum is simply dummy text of the printing and typesetting industry. Lorem Ipsum has been the industry's standard dummy text ever since the 1500s, when an unknown printer took a galley of type and scrambled it to make a type specimen book. It has survived not only five centuries, but also the leap into electronic typesetting, remaining essentially unchanged.Lorem Ipsum is simply dummy text of the printing and typesetting industry. Lorem Ipsum has been the industry's standard dummy text ever since the 1500s, when an unknown printer took a galley of type and scrambled it to make a type specimen book. It has survived not only five centuries, but also the leap into electronic typesetting, remaining essentially unchanged.</p>
  <div class="btn about-btn">Contact Us</div>
</section>

<section>
  <div class="tile" style="left:0;top:1127px;width:300px;background:linear-gradient(180deg,#6d8aa6,#c9d6e2 55%,#3c4b5c)" role="img" aria-label="Glass skyscrapers seen from below"></div>
  <div class="tile" style="left:300px;top:1127px;width:300px;background:linear-gradient(135deg,#e8f1fb,#6aa4e0 60%,#1d5cb8)" role="img" aria-label="Hands using a tablet with blue digital interface"></div>
  <div class="panel panel-blue" style="left:600px;top:1127px;width:600px">
    <h3 style="left:49px">Neque porro quisquam est</h3>
    <p style="left:50px">Lorem Ipsum is simply dummy text of the printing and typesetting industry. Lorem Ipsum has been the industry's standard dummy text ever since the 1500s, when an unknown printer took</p>
    <div class="btn" style="left:51px">Learn More</div>
  </div>

  <div class="panel panel-ink" style="left:0;top:1414px;width:600px">
    <h3 style="left:143px">Neque porro quisquam est</h3>
    <p style="left:144px">Lorem Ipsum is simply dummy text of the printing and typesetting industry. Lorem Ipsum has been the industry's standard dummy text ever since the 1500s, when an unknown printer took</p>
    <div class="btn" style="left:145px">Learn More</div>
  </div>
  <div class="tile" style="left:600px;top:1414px;width:300px;background:linear-gradient(135deg,#f2f2f2,#d9d9d9 60%,#eeeeee)" role="img" aria-label="Business people meeting in round chairs, seen from above"></div>
  <div class="tile" style="left:900px;top:1414px;width:300px;background:radial-gradient(circle at 45% 40%,#f1b77a,#a0582c 40%,#2b2522 80%)" role="img" aria-label="Glowing light bulb with gears held in a hand"></div>

  <div class="tile" style="left:0;top:1701px;width:299px;background:radial-gradient(circle at 40% 50%,#47c2e8,#1a6d96 45%,#13384f 85%)" role="img" aria-label="Businessman touching a ring of digital service icons"></div>
  <div class="panel panel-navy" style="left:299px;top:1701px;width:600px">
    <h3 style="left:99px">Neque porro quisquam est</h3>
    <p style="left:100px">Lorem Ipsum is simply dummy text of the printing and typesetting industry. Lorem Ipsum has been the industry's standard dummy text ever since the 1500s, when an unknown printer took</p>
    <div class="btn" style="left:101px">Learn More</div>
  </div>
  <div class="tile" style="left:899px;top:1701px;width:301px;background:linear-gradient(150deg,#dfe6ee,#8fa8c4 50%,#3f5874)" role="img" aria-label="Hand pointing at charts on a tablet"></div>
</section>

<section>
  <h2 class="t-title">Testimonials</h2>
  <div class="t-sub">Lorem Ipsum is simply dummy text of the printing and typesetting</div>
  <div class="t-card"></div>
  <div class="t-photo" role="img" aria-label="Businesswoman standing by an office window"></div>
  <svg class="t-quote" width="50" height="40" viewBox="0 0 50 40">
    <path d="M4 4h18v8h-9v28H4z M28 4h18v8h-9v28h-9z" fill="#1183cf"/>
  </svg>
  <p class="t-text">Lorem Ipsum is simply dummy text of the printing and typesetting industry. Lorem Ipsum has been the industry's standard dummy text ever since the 1500s, when an unknown printer took a galley of type and</p>
  <div class="t-name">Maren T Ellsworth</div>
  <div class="t-city">Orlando</div>
  <svg class="t-arrow" style="left:126px" viewBox="0 0 34 34"><circle cx="17" cy="17" r="17" fill="#5fb6ec"/><path d="M20 10l-7 7 7 7" stroke="#fff" stroke-width="2" fill="none"/></svg>
  <svg class="t-arrow" style="left:1039px" viewBox="0 0 34 34"><circle cx="17" cy="17" r="17" fill="#1598e3"/><path d="M14 10l7 7-7 7" stroke="#fff" stroke-width="2" fill="none"/></svg>
</section>

<footer>
  <div class="site-footer"></div>
  <div class="footer-brand"><span class="brand-mark"></span>BRIGHT HARBOR</div>
  <div class="news-label">SIGN UP FOR NEWSLETTER</div>
  <form class="newsletter-form" action="mailto:hello@brightharbor.com?subject=Newsletter" method="post" enctype="text/plain">
    <input class="field" type="email" name="email" placeholder="Your Email" aria-label="Your email for the newsletter">
    <button class="send" type="submit">SIGN UP</button>
  </form>
  <form class="contact-form" action="mailto:hello@brightharbor.com?subject=Contact%20request" method="post" enctype="text/plain" aria-label="Contact form">
    <input class="field name" type="text" name="name" placeholder="Your Name" aria-label="Your name">
    <input class="field email" type="email" name="email" placeholder="Your Email" aria-label="Your email">
    <input class="field message" type="text" name="message" placeholder="Your Message" aria-label="Your message">
    <button class="send" type="submit">SEND</button>
  </form>
  <div class="contact-pill">
    <span><svg width="16" height="20" viewBox="0 0 16 20"><path d="M8 0a7 7 0 0 0-7 7c0 5 7 13 7 13s7-8 7-13a7 7 0 0 0-7-7zm0 10a3 3 0 1 1 0-6 3 3 0 0 1 0 6z" fill="#1598e3"/></svg>18, rue des Tilleuls L - 5210 Marnach</span>
    <span>I</span>
    <span><svg width="18" height="18" viewBox="0 0 18 18"><path d="M4 1l3 4-2 2c1 2 3 4 5 5l2-2 4 3-2 3C8 16 2 10 1 4z" fill="#1598e3"/></svg>555-214-7730</span>
    <span>I</span>
    <span><svg width="18" height="14" viewBox="0 0 18 14"><rect width="18" height="14" rx="2" fill="#1598e3"/><path d="M1 2l8 6 8-6" stroke="#0b2346" stroke-width="1.5" fill="none"/></svg>hello@brightharbor.com</span>
  </div>
  <div class="footer-links" style="top:2894px">Home<i>I</i>About US<i>I</i>Services<i>I</i>Clients<i>I</i>Projects<i>I</i>Contact Us</div>
  <div class="footer-links" style="top:2926px">Legal Information<i>I</i>Data Protection (GDPR)<i>I</i>Website Owner Declaration</div>
  <div class="footer-links" style="top:2959px">Bright Harbor © 2021 All Rights Reserved. | &nbsp;Privacy Policy</div>
  <div class="social"><span></span><span></span><span></span><span></span></div>
</footer>

</body>
</html>
```